Brightwave Travel and Tours

Hotel Reservations
Airline Ticketing
Day Tour

My business is a Travel agency. My services are issuing domestic and international tickets. Book room/hotel reservations local/international.
My color preference is apple green/orange/red/blue.
Images of beaches, tickets,luggage.

```html
<!DOCTYPE html>
<html lang="en">
<head>
<meta charset="utf-8">
<title>Brightwave Travel and Tours – Business Card</title>
<link href="https://fonts.googleapis.com/css2?family=Open+Sans:wght@400;600;700&display=swap" rel="stylesheet">
<style>
  :root {
    --stage: #2b2b2d;
    --sky: #35c1eb;
    --sky-light: #4ccbf0;
    --navy: #1a6f96;
    --navy-deep: #13628a;
    --ink: #3f4a52;
    --text-grey: #4a4a4a;
    --paper: #ffffff;
  }
  * { margin: 0; padding: 0; box-sizing: border-box; }
  html, body { width: 1200px; height: 750px; overflow: hidden; }
  body {
    background: var(--stage);
    font-family: "Open Sans", Arial, sans-serif;
    position: relative;
  }
  .card {
    position: absolute;
    top: 220px;
    width: 525px;
    height: 300px;
    overflow: hidden;
    box-shadow: 0 14px 30px rgba(0,0,0,.45);
  }
  /* Front */
  .card--front { left: 45px; background: var(--sky); }
  .brand {
    position: absolute;
    left: 0; right: 0; top: 92px;
    display: flex; align-items: center; justify-content: center; gap: 12px;
  }
  .brand__dot {
    width: 22px; height: 22px; border-radius: 50%;
    background: var(--navy);
    flex: none;
  }
  .brand__name {
    font-weight: 700; font-size: 24px; letter-spacing: .5px;
    color: var(--navy);
  }
  .services {
    position: absolute; left: 0; right: 0; bottom: 36px;
    text-align: center; font-size: 13px; color: var(--ink);
  }
  /* Back */
  .card--back { left: 630px; background: var(--paper); }
  .accent-tab {
    position: absolute; left: 0; top: 44px;
    width: 14px; height: 26px; background: var(--navy);
  }
  .person { position: absolute; left: 42px; top: 30px; }
  .person__name { font-size: 19px; font-weight: 700; color: var(--navy); }
  .person__role { font-size: 14px; color: var(--sky); margin-top: -2px; padding-left: 8px; }
  .contact {
    position: absolute; left: 70px; top: 108px;
    font-size: 12.5px; color: var(--text-grey); line-height: 18px;
    list-style: none;
  }
  .contact__addr { margin-bottom: 10px; padding-left: 22px; }
  .contact li { display: flex; align-items: center; gap: 8px; }
  .contact svg { width: 14px; height: 14px; fill: var(--navy); flex: none; }
  .brand--back {
    left: auto; right: 28px; top: 82px;
    width: 180px;
    flex-direction: column; gap: 8px;
  }
  .brand--back .brand__name {
    font-size: 20px; line-height: 24px; letter-spacing: .3px;
    text-align: center;
  }
  .footer-band { position: absolute; left: 0; bottom: 0; width: 525px; height: 70px; }
</style>
</head>
<body>

<section class="card card--front">
  <div class="brand">
    <span class="brand__dot"></span>
    <span class="brand__name">Brightwave Travel and Tours</span>
  </div>
  <p class="services">Hotel Reservations &bull; Airline Ticketing &bull; Day Tour</p>
</section>

<section class="card card--back">
  <span class="accent-tab"></span>
  <div class="person">
    <h1 class="person__name">Marcus Ellery</h1>
    <p class="person__role">President</p>
  </div>

  <ul class="contact">
    <li class="contact__addr">2217 Harbor View Lane<br>Oakdale, NY 11769</li>
    <li><svg viewBox="0 0 16 16"><path d="M3 2h3l1.5 3.5-2 1.2a8 8 0 0 0 3.8 3.8l1.2-2L14 10v3a1 1 0 0 1-1 1A11 11 0 0 1 2 3a1 1 0 0 1 1-1z"/></svg>631 555 0148</li>
    <li><svg viewBox="0 0 16 16"><path d="M5 1h6a1 1 0 0 1 1 1v12a1 1 0 0 1-1 1H5a1 1 0 0 1-1-1V2a1 1 0 0 1 1-1zm.5 2v9h5V3zm2.5 10a.8.8 0 1 0 0 .1z"/></svg>631 555 0172</li>
    <li><svg viewBox="0 0 16 16"><path d="M4 1h7v4H4zM2 6h12a1 1 0 0 1 1 1v6H1V7a1 1 0 0 1 1-1zm2 4h8v2H4z"/></svg>631 555 0193</li>
    <li><svg viewBox="0 0 16 16"><path d="M1 3h14v10H1zm1.5 1.5L8 9l5.5-4.5V4h-11z"/></svg>marcus@brightwavetravel.com</li>
    <li><svg viewBox="0 0 16 16"><path d="M8 1a7 7 0 1 0 0 14A7 7 0 0 0 8 1zm0 1.5c.8 0 1.7 1.5 2 4H6c.3-2.5 1.2-4 2-4zM6 8.5h4c-.3 2.5-1.2 4-2 4s-1.7-1.5-2-4z"/></svg>www.brightwavetravel.com</li>
  </ul>

  <div class="brand brand--back">
    <span class="brand__dot"></span>
    <span class="brand__name">Brightwave<br>Travel and Tours</span>
  </div>

  <svg class="footer-band" viewBox="0 0 525 70" preserveAspectRatio="none" aria-hidden="true">
    <polygon points="0,70 0,58 300,58 360,30 525,30 525,70" fill="var(--navy-deep)"/>
    <polygon points="305,58 525,58 525,36 362,36" fill="var(--navy)"/>
    <polygon points="420,36 525,36 525,58 420,58" fill="var(--sky-light)"/>
    <rect x="415" y="36" width="4" height="22" fill="var(--paper)"/>
  </svg>
</section>

</body>
</html>
```